New National Dermatology Group needs a business card!

We need a business card for our new national company that has 3 brands within the business:
Brellow Clinics Australia, Tamvirk Clinics Australia and Orvandel Clinics Australia.
We help people access dermatology services close to home throughout Australia.
We need a business card that has:
all 3 logos on it,
Our websites (there are three, listed above)
Our email (there are three, listed above)
The location of our first clinic: 41 Wendle St Parramatta (this can then be changed for each location as required)

```html
<!DOCTYPE html>
<html lang="en">
<head>
<meta charset="utf-8">
<title>Dermatology Group Business Card</title>
<link rel="stylesheet" href="https://fonts.googleapis.com/css2?family=Poppins:wght@400;500&display=swap">
<style>
  :root {
    --bg: #c4c4c4;
    --brown: #7b3c1b;
    --brown-light: #9a4f25;
    --green: #1fae4b;
    --orange: #f58a2c;
    --ink: #1d1d1d;
    --rule: #444;
    --white: #ffffff;
  }
  * { margin: 0; padding: 0; box-sizing: border-box; }
  html, body { width: 1200px; height: 1200px; overflow: hidden; }
  body {
    background: var(--bg);
    font-family: "Poppins", sans-serif;
    position: relative;
  }
  .card {
    position: absolute;
    top: 303px;
    width: 368px;
    height: 593px;
  }
  .card-front {
    left: 200px;
    background: radial-gradient(ellipse at 50% 50%, var(--brown-light) 0%, var(--brown) 85%);
  }
  .card-back {
    left: 599px;
    background: var(--white);
  }
  .brand-name {
    position: absolute;
    left: 0;
    width: 100%;
    text-align: center;
    font-weight: 500;
    line-height: 1;
  }
  .brand-name .word {
    display: block;
    font-size: 36px;
    letter-spacing: 2px;
  }
  .brand-name .sub {
    display: block;
    margin-top: 8px;
    font-size: 11px;
    letter-spacing: 5px;
  }
  .card-front .brand-name { color: var(--white); }
  .brand-block {
    position: absolute;
    left: 0;
    width: 100%;
    height: 175px;
  }
  .brand-block .brand-name { top: 0; }
  .brand-block .brand-name .word { font-size: 32px; }
  .side-bar {
    position: absolute;
    top: 0;
    width: 10px;
    height: 50px;
  }
  .side-bar.left { left: 0; }
  .side-bar.right { right: 0; }
  .icon-row {
    position: absolute;
    top: 70px;
    left: 0;
    width: 100%;
    display: flex;
    justify-content: center;
    align-items: center;
    gap: 10px;
  }
  .icon-row .rule {
    width: 36px;
    height: 1px;
    background: var(--rule);
    margin: 0 12px;
  }
  .contact {
    position: absolute;
    top: 88px;
    left: 0;
    width: 100%;
    text-align: center;
    color: var(--ink);
    font-size: 16.5px;
    line-height: 21px;
    font-weight: 400;
  }
  .contact .address { margin-top: 8px; }
  .brand-orvandel { color: var(--brown); }
  .brand-brellow { color: var(--green); }
  .brand-tamvirk { color: var(--orange); }
  .bar-orvandel { background: var(--brown); }
  .bar-brellow { background: var(--green); }
  .bar-tamvirk { background: var(--orange); }
</style>
</head>
<body>

<section class="card card-front">
  <div class="brand-name" style="top: 82px;">
    <span class="word">ORVANDEL</span>
    <span class="sub">CLINICS AUSTRALIA</span>
  </div>
  <div class="brand-name" style="top: 259px;">
    <span class="word">BRELLOW</span>
    <span class="sub">CLINICS AUSTRALIA</span>
  </div>
  <div class="brand-name" style="top: 433px;">
    <span class="word">TAMVIRK</span>
    <span class="sub">CLINICS AUSTRALIA</span>
  </div>
</section>

<section class="card card-back">
  <div class="brand-block" style="top: 42px;">
    <span class="side-bar left bar-orvandel"></span>
    <span class="side-bar right bar-orvandel"></span>
    <div class="brand-name brand-orvandel">
      <span class="word">ORVANDEL</span>
      <span class="sub">CLINICS AUSTRALIA</span>
    </div>
    <div class="icon-row brand-orvandel">
      <span class="rule"></span>
      <svg width="16" height="12" viewBox="0 0 16 12"><rect x="0.5" y="0.5" width="15" height="11" fill="currentColor"/><path d="M0.5 0.5 L8 7 L15.5 0.5" fill="none" stroke="#fff" stroke-width="1.2"/></svg>
      <svg width="14" height="14" viewBox="0 0 14 14" fill="none" stroke="currentColor" stroke-width="1.3"><circle cx="7" cy="7" r="6"/><ellipse cx="7" cy="7" rx="2.6" ry="6"/><path d="M1 7h12M2 4h10M2 10h10"/></svg>
      <span class="rule"></span>
    </div>
    <div class="contact">
      <p>info@orvandel.co.uk</p>
      <p>www.orvandel.co.uk</p>
      <p class="address">41 Wendle St Parramatta</p>
    </div>
  </div>

  <div class="brand-block" style="top: 227px;">
    <span class="side-bar left bar-brellow"></span>
    <span class="side-bar right bar-brellow"></span>
    <div class="brand-name brand-brellow">
      <span class="word">BRELLOW</span>
      <span class="sub">CLINICS AUSTRALIA</span>
    </div>
    <div class="icon-row brand-brellow">
      <span class="rule"></span>
      <svg width="16" height="12" viewBox="0 0 16 12"><rect x="0.5" y="0.5" width="15" height="11" fill="currentColor"/><path d="M0.5 0.5 L8 7 L15.5 0.5" fill="none" stroke="#fff" stroke-width="1.2"/></svg>
      <svg width="14" height="14" viewBox="0 0 14 14" fill="none" stroke="currentColor" stroke-width="1.3"><circle cx="7" cy="7" r="6"/><ellipse cx="7" cy="7" rx="2.6" ry="6"/><path d="M1 7h12M2 4h10M2 10h10"/></svg>
      <span class="rule"></span>
    </div>
    <div class="contact">
      <p>info@brellow.co.uk</p>
      <p>www.brellow.co.uk</p>
      <p class="address">41 Wendle St Parramatta</p>
    </div>
  </div>

  <div class="brand-block" style="top: 412px;">
    <span class="side-bar left bar-tamvirk"></span>
    <span class="side-bar right bar-tamvirk"></span>
    <div class="brand-name brand-tamvirk">
      <span class="word">TAMVIRK</span>
      <span class="sub">CLINICS AUSTRALIA</span>
    </div>
    <div class="icon-row brand-tamvirk">
      <span class="rule"></span>
      <svg width="16" height="12" viewBox="0 0 16 12"><rect x="0.5" y="0.5" width="15" height="11" fill="currentColor"/><path d="M0.5 0.5 L8 7 L15.5 0.5" fill="none" stroke="#fff" stroke-width="1.2"/></svg>
      <svg width="14" height="14" viewBox="0 0 14 14" fill="none" stroke="currentColor" stroke-width="1.3"><circle cx="7" cy="7" r="6"/><ellipse cx="7" cy="7" rx="2.6" ry="6"/><path d="M1 7h12M2 4h10M2 10h10"/></svg>
      <span class="rule"></span>
    </div>
    <div class="contact">
      <p>info@tamvirk.co.uk</p>
      <p>www.tamvirk.co.uk</p>
      <p class="address">41 Wendle St Parramatta</p>
    </div>
  </div>
</section>

</body>
</html>
```